Velmor PashuのRTZの電子書籍表紙デザインをお願いします。

*週末ごとに和みを探す読者へ贈る癒やしの四季手帳*というタイトルの表紙デザインの発注です。
サブタイトル 猫の昼寝は街を照らす
猫の昼寝は毎日を照らす
私は猫の昼寝に癒された
になります。
お笑い要素の多い1日1笑いみたいな本の表紙です。

初めての表紙デザイン依頼なので、よく勝手がわかっていませんので、
出来上がったデザインを作家グループの中で投票にかけて、
一番投票得票数の多かったものを表紙デザインとして選ばせていただきたいと考えております。
もしかしたら、その中で、何か修正依頼など来るかもしれませんが、
それも含めて、ご対応していただける方よろしくお願いします。

1部内容の抜粋を記載します。

その他何かご不明な点がございましたら、お気軽にご質問下さい。
よろしくお願いいたします。
すいません。作家名は後でお伝えします。作家名もどこかに挿入いただきたいです。よろしくお願いします。
データサイズですが、推奨サイズでJPEGファイルでご納品下さい、よろしくお願いします。
皆様、たくさんのご応募まことにありがとうございました。
現在、作家グループへ全体回覧のメールを致しました。
皆様の投票結果までお待ちください。
また、この度、いろいろな作品に触れさせていただきましたこと本当に
本当に感謝いたします。
今回の表紙に関しましては、どうしても1名しか選べない状況がございますこと
また、選挙による投票にて決定致しますこと、ご理解何卒よろしくお願い申しあげます。
また、もしも、今回当選に至らないことがありましても、
今後も私自身は作家生活を継続予定ですので、
(今回は作品の表紙に合わないことがあっても)作風の気に入ったデザイナー様には
個人的にお話を相談させていただく場合もあると思っております。
その際には何卒よろしくお願い申し上げます。この度はまことにありがとうございました。
この度はご応募まことにありがとうございました。厳選なる選挙の結果、1名の作家さんが選ばれました。
選ばれました方には個別にお伝えいたしております。この度はまことにご応募ありがとうございました。

作家メンバーによる総選挙にて決定させて頂きました。皆様に広く愛される作品で、投票数も多く選ばせて頂きました。誠にありがとうございました。

今回、誠にご提案ありがとうございました。私自身は作家活動を継続していくつもりですので、また、個別にご依頼させて頂くこともあるかと思います。その時はよろしくお願いします。この度はありがとうございました。

```html
<!DOCTYPE html>
<html lang="ja">
<head>
<meta charset="utf-8">
<title>週末ごとに和みを探す読者へ贈る癒やしの四季手帳</title>
<link rel="stylesheet" href="https://fonts.googleapis.com/css2?family=Mochiy+Pop+One&display=swap">
<style>
  :root {
    --bg-orange: #f6a234;
    --circle-purple: #8e74c8;
    --ribbon-yellow: #fff200;
    --title-red: #ee2a2a;
    --title-yellow: #ffe600;
    --box-blue: #1f5fd0;
    --ink: #1a1a1a;
    --paper: #ffffff;
  }
  html, body { margin: 0; padding: 0; overflow: hidden; }
  body { width: 750px; height: 1200px; background: var(--bg-orange); }
  .cover {
    position: relative; width: 750px; height: 1200px; overflow: hidden;
    background: var(--bg-orange);
    font-family: "Mochiy Pop One", sans-serif;
  }
  .cover h1, .cover p { margin: 0; font-weight: 400; }
  .photo-area {
    position: absolute; left: 110px; top: 500px; width: 530px; height: 530px;
    border-radius: 50%;
    background: radial-gradient(circle at 50% 58%, #fbf7ef 0%, #efe6d8 38%, #b7a4dc 62%, var(--circle-purple) 72%);
  }
  .tagline-box {
    position: absolute; left: 22px; top: 70px; padding: 4px 12px;
    background: var(--paper); border: 5px solid var(--ink); border-radius: 14px;
    font-size: 32px; line-height: 1.3; color: var(--ink); transform: rotate(-10deg);
    white-space: nowrap;
  }
  .lead {
    position: absolute; font-size: 56px; line-height: 1; color: var(--ink);
    -webkit-text-stroke: 2px var(--paper); paint-order: stroke fill; white-space: nowrap;
  }
  .lead.one { left: 250px; top: 22px; }
  .lead.two { left: 270px; top: 100px; }
  .title-main {
    position: absolute; left: 280px; top: 195px; font-size: 80px; line-height: 1;
    color: var(--title-red); white-space: nowrap;
    -webkit-text-stroke: 12px var(--title-yellow); paint-order: stroke fill;
  }
  .season-box {
    position: absolute; display: flex; align-items: center; justify-content: center;
    background: var(--title-yellow); color: var(--box-blue); border: 6px solid var(--box-blue);
    line-height: 1;
  }
  .season-box.big { left: 80px; top: 315px; width: 110px; height: 110px; font-size: 80px; border-radius: 8px; }
  .season-box.small { left: 240px; top: 335px; width: 90px; height: 95px; font-size: 64px; border-radius: 6px; transform: rotate(6deg); }
  .title-end {
    position: absolute; left: 130px; top: 418px; font-size: 118px; line-height: 1;
    color: var(--title-red); letter-spacing: 20px; white-space: nowrap;
    -webkit-text-stroke: 14px var(--title-yellow); paint-order: stroke fill;
  }
  .ribbon {
    position: absolute; background: var(--ribbon-yellow); color: var(--ink);
    font-size: 28px; line-height: 1;
    writing-mode: vertical-rl; text-orientation: upright;
    padding: 14px 10px; white-space: nowrap;
  }
  .ribbon.upper-right { left: 664px; top: 130px; transform: rotate(-10deg); }
  .ribbon.lower-right { left: 670px; top: 560px; transform: rotate(-6deg); }
  .ribbon.left { left: 22px; top: 620px; transform: rotate(8deg); }
  .author {
    position: absolute; left: 525px; top: 1118px; font-size: 38px; line-height: 1;
    color: var(--ink); letter-spacing: 6px; white-space: nowrap;
    -webkit-text-stroke: 6px var(--paper); paint-order: stroke fill;
  }
</style>
</head>
<body>
<main class="cover">
  <div class="photo-area" role="img" aria-label="紫の円を背景に、目を細めて笑う白い犬の写真"></div>
  <div class="tagline-box">週末ごとに</div>
  <div class="lead one">和みを探す</div>
  <div class="lead two">読者へ贈る</div>
  <h1 class="title-main">癒やしの</h1>
  <div class="season-box big">四</div>
  <div class="season-box small">季</div>
  <div class="title-end">手帳</div>
  <p class="ribbon upper-right">猫の昼寝は街を照らす</p>
  <p class="ribbon lower-right">猫の昼寝は毎日を照らす</p>
  <p class="ribbon left">私は猫の昼寝に癒された</p>
  <div class="author">桐谷光陽</div>
</main>
</body>
</html>
```